Bref créative
Bath/Spa Product Label
Vesta Reef
Thanks to you expert graphic artists we have been happy with the logo designed last summer and would like to see what you wizards can do to with a product label.
We have attached the current logo and would love to see what you can do with creating a product label that will fit several types of labels.
1. We need a vertical orientation of the label to be scalable so that we can use it on 16 oz or 8 ounce bottles.
2. We need a horizontal orientation that is also scalable for 8 ounce or 4 ounce jars.
You can place the uploaded logo anywhere on the labels but we need blank space to fill in the product name, net weight, instructions and ingredients.
Feel free to apply generic text for the net weight, instructions and ingredients. We manufacture shampoos, conditioners, body washes, shower gels, body scrubs, foot scrubs, sugar scrubs, etc.
We have attached two sample MS Word documents with the ugly and boring labels we use now. Use these as inspiration to move us to the next level. Go ahead add color, fonts, additional graphics - whatever you see fit. In the past, we have treated our designers fairly and cordially. You can expect the same treatment for this contest.
Personal Care
Over 95% of our customer base is women. But keep in mind that men also use shower gels - so no teddy bears on the product label please.Our clients are used to high quality product, not over hyped claims or garish designs.
As stated above we need the label in at least two orientations. It must also be scalable so that we can use it on different size labels. If you can design a third label in square dimensions that would be a big bonus.
Current jar label - for example DO NOT REPLICATE.
Sample shampoo/body wash label applied vertically to 16 ounce or 8 ounce bottles. FOR EXAMPLE ONLY DO NOT REPLICATE
Current logo - DO NOT DISTRIBUTE - COPYRIGHT VESTA REEF.

```html
<!DOCTYPE html>
<html lang="en">
<head>
<meta charset="utf-8">
<title>Vesta Reef – Glistening Sugar Scrub Label</title>
<link href="https://fonts.googleapis.com/css2?family=Cinzel:wght@500&family=Playfair+Display:ital@1&family=Open+Sans:wght@400;600&display=swap" rel="stylesheet">
<style>
  :root {
    --stage: #2b2b2d;
    --purple-deep: #4a2a78;
    --purple-mid: #7c5aae;
    --purple-light: #b9a2dc;
    --magenta: #a3186c;
    --pink: #e05aa6;
    --cream: #fff6d8;
    --cream-warm: #f7e3a6;
    --lavender: #cbb8e6;
    --gold: #c99a2e;
    --title: #6a3f9a;
    --box-fill: rgba(215, 200, 238, 0.72);
    --ink: #3d2a5a;
    --white: #ffffff;
  }
  * { margin: 0; padding: 0; box-sizing: border-box; }
  html, body { width: 1200px; height: 826px; overflow: hidden; background: var(--stage); }
  .label {
    position: absolute; left: 50px; top: 55px; width: 1100px; height: 716px;
    font-family: "Open Sans", Arial, sans-serif; color: var(--ink);
  }
  .label-art { position: absolute; inset: 0; width: 1100px; height: 716px; }
  .model-photo {
    position: absolute; left: 25px; top: 99px; width: 198px; height: 213px;
    background: linear-gradient(160deg, #e9d2c0 0%, #c59a7f 55%, #8a6a8e 100%);
  }
  .blurb {
    position: absolute; left: 41px; top: 312px; width: 255px; height: 143px;
    background: var(--box-fill); padding: 14px 16px;
    font-size: 15px; line-height: 1.4; text-align: center;
  }
  .facts {
    position: absolute; left: 741px; top: 89px; width: 230px; height: 254px;
    background: var(--box-fill); padding: 12px 14px;
    font-size: 12.5px; line-height: 1.38; text-align: justify;
  }
  .facts p + p { margin-top: 12px; }
  .facts .heading { display: block; }
  .brand {
    position: absolute; left: 327px; top: 250px; width: 373px; text-align: center;
  }
  .brand-mark {
    width: 34px; height: 34px; border-radius: 50%; background: var(--gold);
    margin: 0 auto 14px;
  }
  .brand-name {
    font-family: "Cinzel", Georgia, serif; font-weight: 500; font-size: 44px;
    letter-spacing: 3px; color: var(--gold);
  }
  .product-name {
    position: absolute; left: 357px; top: 450px; width: 313px;
    font-family: "Playfair Display", Georgia, serif; font-style: italic;
    font-size: 27px; line-height: 1.42; color: var(--title); text-align: center;
  }
  .net-weight {
    position: absolute; left: 327px; top: 668px; width: 373px; text-align: center;
    font-size: 15px; color: var(--white);
  }
</style>
</head>
<body>
<main class="label">
  <svg class="label-art" viewBox="0 0 1100 716" aria-hidden="true">
    <defs>
      <radialGradient id="bgGlow" cx="0.5" cy="0.45" r="0.75">
        <stop offset="0" stop-color="var(--purple-light)"/>
        <stop offset="0.55" stop-color="var(--purple-mid)"/>
        <stop offset="1" stop-color="var(--purple-deep)"/>
      </radialGradient>
      <linearGradient id="panelFill" x1="0" y1="0" x2="0" y2="1">
        <stop offset="0" stop-color="var(--cream)"/>
        <stop offset="0.52" stop-color="var(--cream-warm)"/>
        <stop offset="0.6" stop-color="var(--lavender)"/>
        <stop offset="1" stop-color="#a88fd0"/>
      </linearGradient>
    </defs>
    <rect class="label-ground" width="1100" height="716" fill="url(#bgGlow)"/>
    <rect class="band-top" y="12" width="1100" height="14" fill="var(--magenta)"/>
    <rect class="band-top-line" y="8" width="1100" height="3" fill="var(--pink)"/>
    <rect class="band-bottom" y="694" width="1100" height="14" fill="var(--magenta)"/>
    <rect class="band-bottom-line" y="709" width="1100" height="3" fill="var(--pink)"/>
    <path class="panel-border" d="M316,660 V186 C316,142 372,130 424,100 C470,74 502,58 513,28 C524,58 556,74 602,100 C654,130 711,142 711,186 V660 Z" fill="none" stroke="var(--white)" stroke-width="2"/>
    <path class="panel" d="M327,650 V190 C327,150 380,140 430,110 C475,85 505,70 513,41 C521,70 551,85 596,110 C646,140 700,150 700,190 V650 Z" fill="url(#panelFill)"/>
    <line x1="345" y1="430" x2="682" y2="430" stroke="var(--white)" stroke-width="1.5"/>
    <line x1="345" y1="630" x2="682" y2="630" stroke="var(--white)" stroke-width="1.5"/>
  </svg>

  <div class="model-photo" role="img" aria-label="Portrait photo of a smiling woman touching her cheek"></div>

  <p class="blurb">A unique blend of safflower oil, sugar and jojoba beads, to exfoliate and bring a lovely glow to your skin. Scented with invigorating Lavender Mint.</p>

  <div class="facts">
    <p><span class="heading">Ingredients:</span> Sucrose, Carthamus tinctorius (Safflower) Seed Oil, Polysorbate 80, Tocopheryl Acetate (Vitamin E), Fragrance, Silica, Phenoxyethanol.</p>
    <p><span class="heading">WARNING:</span> This product contains natural oils that can make surfaces slippery. Use caution whenever using this product to prevent possible injury.</p>
  </div>

  <div class="brand">
    <div class="brand-mark"></div>
    <div class="brand-name">VESTA REEF</div>
  </div>

  <h1 class="product-name">Glistening Sugar Scrub with Jojoba Beads and Lavender Mint Scent</h1>

  <p class="net-weight">150 gram</p>
</main>
</body>
</html>
```